Pull-Up Banner for creating escape room themed engaging learning experiences

Our research group create engaging learning experiences aimed at the following markets: Primary school, secondary school, tertiary and corporate training. We want learning to be fun, but also deep - where participants will need to think deeply and apply themselves to solve problems as a team.
We are the inventors of the open source escape room decoder box and want to engage students in learning in a fun way which maximizes teamwork. We are also keen to be contracted to design custom escape room learning experiences for corporate entities to engage their staff and have them working together as a team.

```html
<!DOCTYPE html>
<html lang="en">
<head>
<meta charset="utf-8">
<title>Puzzle Lab Learning – Pull-Up Banner</title>
<link href="https://fonts.googleapis.com/css2?family=Roboto+Condensed:wght@400;700&display=swap" rel="stylesheet">
<style>
  :root {
    --stage: #e4e5e8;
    --panel-grey: #d3d4d6;
    --panel-grey-dark: #b9babd;
    --brand-blue: #2e8fd6;
    --deep-blue: #0e57a4;
    --accent-red: #ec2330;
    --brand-orange: #f39020;
    --ink: #1c1c1c;
    --white: #ffffff;
  }
  * { box-sizing: border-box; margin: 0; padding: 0; }
  html, body { width: 1200px; height: 1200px; overflow: hidden; }
  body {
    background: var(--stage);
    font-family: "Roboto Condensed", "Arial Narrow", sans-serif;
    position: relative;
  }
  .banner {
    position: absolute;
    left: 338px; top: 30px;
    width: 523px; height: 1140px;
    background: var(--panel-grey);
    overflow: hidden;
  }
  .banner-backdrop {
    position: absolute; left: 0; top: 380px; width: 100%; height: 560px;
    background: radial-gradient(ellipse at 40% 30%, #c6c7ca 0%, #d3d4d6 55%, #cfd0d3 100%);
  }
  .hero-photo {
    position: absolute; left: 0; top: 0; width: 100%; height: 400px;
    background: linear-gradient(160deg, #e9e6e1 0%, #cdbfae 40%, #8a7a68 70%, #e8e4dc 100%);
  }
  .hero-shapes { position: absolute; left: 0; top: 0; width: 523px; height: 400px; }
  .brand {
    position: absolute; left: 40px; top: 450px; width: 443px;
    display: flex; align-items: center; gap: 16px;
  }
  .brand-dot {
    width: 70px; height: 70px; border-radius: 50%;
    background: var(--brand-blue); flex: none;
  }
  .brand-name {
    font-weight: 700; font-size: 44px; line-height: 1;
    color: var(--brand-orange); text-transform: uppercase; letter-spacing: 0.5px;
  }
  .intro {
    position: absolute; left: 40px; top: 590px; width: 441px;
    color: var(--ink); font-size: 16.6px; line-height: 20.5px;
    text-align: justify;
  }
  .intro p + p { margin-top: 20px; }
  .contact-band {
    position: absolute; left: 0; top: 930px; width: 100%; height: 210px;
    background: var(--brand-blue);
  }
  .gallery { position: absolute; left: 0; top: 852px; width: 100%; height: 152px; }
  .gallery-photo {
    position: absolute; top: 0; width: 148px; height: 148px; border-radius: 50%;
    border: 5px solid var(--brand-orange);
    box-shadow: 0 0 0 4px #e9e9ea;
  }
  .gallery-photo.team-table { left: 20px; background: linear-gradient(140deg, #d9d4cc, #8d8a86 60%, #4a4442); }
  .gallery-photo.group-play { left: 187px; background: linear-gradient(140deg, #3a3540, #6a2c30 45%, #2f3847); }
  .gallery-photo.decoder-box { left: 350px; background: linear-gradient(140deg, #4a2a26, #b0453c 40%, #d9d4cf 70%, #2a2a2a); }
  .phone {
    position: absolute; left: 0; top: 1004px; width: 100%;
    text-align: center; color: var(--brand-orange);
    font-weight: 700; font-size: 74px; line-height: 1; letter-spacing: -1px;
  }
  .web {
    position: absolute; left: 0; top: 1086px; width: 100%;
    text-align: center; color: var(--white); font-size: 28px; line-height: 1;
  }
</style>
</head>
<body>
  <div class="banner">
    <div class="banner-backdrop" role="img" aria-label="Faded photo of students working on a puzzle"></div>
    <div class="hero-photo" role="img" aria-label="Photo of a facilitator helping three women solve an escape room puzzle at a table"></div>
    <svg class="hero-shapes" viewBox="0 0 523 400" aria-hidden="true">
      <polygon points="0,400 0,392 523,300 523,400" fill="var(--panel-grey)"/>
      <polygon points="0,281 209,335 0,380" fill="var(--deep-blue)"/>
      <polygon points="20,388 523,271 523,304 60,385" fill="var(--accent-red)"/>
    </svg>

    <div class="brand">
      <span class="brand-dot"></span>
      <span class="brand-name">Puzzle Lab Learning</span>
    </div>

    <div class="intro">
      <p>Our research group create engaging learning experiences aimed at the following markets: Primary school, secondary school, tertiary and corporate training. We want learning to be fun, but also deep - where participants will need to think deeply and apply themselves to solve problems as a team.</p>
      <p>We are the inventors of the open source escape room decoder box and want to engage students in learning in a fun way which maximizes teamwork. We are also keen to be contracted to design custom escape room learning experiences for corporate entities to engage their staff and have them working together as a team</p>
    </div>

    <div class="contact-band"></div>
    <div class="gallery">
      <div class="gallery-photo team-table" role="img" aria-label="Photo of a small group working together at a table"></div>
      <div class="gallery-photo group-play" role="img" aria-label="Photo of students solving clues in a dark escape room"></div>
      <div class="gallery-photo decoder-box" role="img" aria-label="Photo of hands using a decoder box with a red light"></div>
    </div>
    <div class="phone">020 0000 5678</div>
    <div class="web">www.puzzlelablearning.com</div>
  </div>
</body>
</html>
```